依頼詳細
定期的に開催する譲渡会イベントのチラシを会場周辺の住宅等に配布し、保護犬の存在を知らない人にも知って頂けるようにチラシ作成(A4サイズ)のご協力をお願い致します。
記載項目
イベントタイトル ⇒ ほほえみ巡りの道
愛犬同伴可能・入場料無料
開催日時 ⇒ ●年●月●日(●)●時~●時
開催会場 ⇒ Sunny Pawz 東大阪会場 (住所:●●●●)
開催内容 ⇒ 保護犬の新しいお家探し
トリマーによるワンコインお手入れ
わんちゃん用品フリマ販売
わんちゃんオリジナルプリントグッズ受注会(※1)
注意事項 ⇒ 当日の参加犬はPicsnapにてご確認お願い致します。
イベント内容は変更になる場合があります。
愛犬同伴の場合、マナー用品の着用をお願い致します。
会場が狭いため、入場制限を行う場合がございます。
検温・アルコール消毒・マスク着用のご協力をお願い致します。
主催 ⇒ 特定非営利活動法人Sunny Pawz
〒579-2208 枚方市桜木台四丁目3番21号
HP https://sunnypawz2019.example-site.jp/
Picsnap sunnypawz.2019
サイズ
A4
ページ数
片面
希望イメージ
シンプル 複雑
単色 カラフル
暗い 明るい
日常 高級
遊び心 厳粛
未来的 伝統的
女性的 男性的
希望する色
カラフル
納品ファイル
• 高解像度JPG (.jpg)
• イラストレーター形式 (.ai)
補足説明
開催日時・会場は、イベントごとに変更して使用させて頂きたいと思っていますので、標準的なフォントでの作成をお願い致します。
その他、フリーイラストやフリー写真を使用して頂いて大丈夫です。

記載内容追加
開催内容の一番最後に、当日の売上金は保護犬の活動費となります。(※1については一部)
ホームページ・PicsnapのQRコード記載をお願い致します。
■ 選んだ理由

文字と写真(イラスト)のバランスや、お伝え出来ていなかったカラーイメージも、当団体のSNS等を拝見してくださって作って頂けたのかなと思い、とても嬉しくなりました。
スタッフ全員での選考を行い、全員が気に入ったため、こちらの提案を当選とさせて頂きました。
度重なる修正依頼にも迅速にご対応頂けて、とても感謝しております。

■ 提案者全員のお礼・コメント

この度、ご提案頂きました皆様、本当にありがとうございました。
皆様の技術のお力をお借りするのに、十分とは言えない金額だったにも関わらず、沢山のご提案を頂けましたこと、感謝しております。

```html
<!DOCTYPE html>
<html lang="ja">
<head>
<meta charset="utf-8">
<title>ほほえみ巡りの道 保護犬譲渡会</title>
<link rel="stylesheet" href="https://fonts.googleapis.com/css2?family=Kiwi+Maru:wght@400;500&family=M+PLUS+Rounded+1c:wght@400;700;800&display=swap">
<style>
:root{
  --stripe:#cfeae2;
  --paper:#ffffff;
  --ink:#5e5e5e;
  --ink-soft:#8a8a8a;
  --mint:#7fc6b4;
  --pink:#ec6f93;
  --star:#f6cf3d;
  --label:#9a9a9a;
}
*{margin:0;padding:0;box-sizing:border-box}
html,body{width:849px;height:1200px;overflow:hidden}
body{font-family:"M PLUS Rounded 1c",sans-serif;color:var(--ink);
  background:repeating-linear-gradient(-45deg,var(--stripe) 0 34px,var(--paper) 34px 68px);position:relative}
.star{position:absolute;fill:var(--star)}
.badge{position:absolute;right:28px;top:14px;text-align:right;color:var(--pink);
  font-weight:800;font-size:25px;line-height:1.3;transform:rotate(-8deg)}
.panel{position:absolute;left:64px;top:80px;width:721px;height:1045px;background:var(--paper);
  border-radius:360px 360px 10px 10px}
.subtitle{position:absolute;top:166px;left:0;width:849px;text-align:center;font-size:19px;letter-spacing:3px}
.title{position:absolute;top:196px;left:0;width:849px;text-align:center;font-family:"Kiwi Maru",serif;
  font-size:60px;font-weight:500;color:var(--ink-soft);letter-spacing:6px}
.deco-line{position:absolute;top:284px;left:160px;width:530px;border-top:2px dashed var(--mint)}
.info{position:absolute;top:310px;display:flex;gap:10px}
.info-label{width:30px;background:var(--label);color:#fff;font-size:15px;writing-mode:vertical-rl;
  display:flex;align-items:center;justify-content:center;letter-spacing:6px;border-radius:3px}
.date{left:150px}
.date .year{font-size:19px}
.date .day{font-size:50px;font-weight:800;line-height:1}
.date .day small{font-size:20px}
.date .time{font-size:32px;font-weight:700}
.place{left:430px}
.place .venue{font-size:23px;font-weight:700;margin-top:10px}
.place .addr{font-size:14px;margin-top:10px;line-height:1.5}
.photos{position:absolute;top:440px;left:215px;display:grid;grid-template-columns:200px 200px;gap:10px}
.photo{height:120px;border-radius:4px}
.p1{background:linear-gradient(135deg,#f1d7b4,#c99a66)}
.p2{background:linear-gradient(135deg,#e8c89a,#b5804e)}
.p3{background:linear-gradient(135deg,#d49a6a,#9a5e35)}
.p4{background:linear-gradient(135deg,#f0dcc0,#c7a07a)}
.waiting{position:absolute;left:636px;top:466px;color:var(--pink);font-weight:800;font-size:20px;transform:rotate(12deg)}
.paw{position:absolute;fill:#d6d6d6}
.section{position:absolute;left:100px;display:flex;gap:24px}
.pill{width:105px;height:30px;background:var(--label);color:#fff;border-radius:15px;font-size:14px;
  display:flex;align-items:center;justify-content:center;flex-shrink:0;margin-top:10px}
.events{top:700px}
.event-list{list-style:none;font-size:21px;font-weight:700;line-height:1.75}
.event-list li{display:flex;align-items:center;gap:10px}
.event-list svg{width:22px;height:22px;fill:var(--pink)}
.event-list sup{font-size:11px}
.notes{top:878px}
.note-list{list-style:none;font-size:14px;line-height:1.7}
.note-list li::before{content:"・";color:var(--mint)}
.footer{position:absolute;left:90px;top:1010px;display:flex;gap:16px;align-items:center}
.org-mark{display:flex;align-items:center;gap:6px;font-weight:800;font-size:17px;color:var(--pink)}
.org-mark span.dot{width:18px;height:18px;border-radius:50%;background:var(--mint)}
.org-text{font-size:11.5px;line-height:1.55}
.footnote{position:absolute;left:230px;top:1095px;font-size:11px;color:var(--ink-soft)}
</style>
</head>
<body>
<svg class="star" style="left:60px;top:40px" width="40" height="40" viewBox="0 0 24 24"><path d="M12 2l3 7 7 .6-5.4 4.6 1.7 7.3L12 17.6 5.7 21.5l1.7-7.3L2 9.6 9 9z"/></svg>
<svg class="star" style="left:160px;top:90px" width="28" height="28" viewBox="0 0 24 24"><path d="M12 2l3 7 7 .6-5.4 4.6 1.7 7.3L12 17.6 5.7 21.5l1.7-7.3L2 9.6 9 9z"/></svg>
<svg class="star" style="left:30px;top:150px" width="24" height="24" viewBox="0 0 24 24"><path d="M12 2l3 7 7 .6-5.4 4.6 1.7 7.3L12 17.6 5.7 21.5l1.7-7.3L2 9.6 9 9z"/></svg>
<svg class="star" style="left:540px;top:60px" width="30" height="30" viewBox="0 0 24 24"><path d="M12 2l3 7 7 .6-5.4 4.6 1.7 7.3L12 17.6 5.7 21.5l1.7-7.3L2 9.6 9 9z"/></svg>
<svg class="star" style="left:740px;top:200px" width="36" height="36" viewBox="0 0 24 24"><path d="M12 2l3 7 7 .6-5.4 4.6 1.7 7.3L12 17.6 5.7 21.5l1.7-7.3L2 9.6 9 9z"/></svg>

<div class="badge">入場無料♪<br>愛犬同伴可能♪</div>

<div class="panel"></div>
<p class="subtitle">保護犬譲渡会</p>
<h1 class="title">ほほえみ巡りの道</h1>
<div class="deco-line"></div>

<div class="info date">
  <div class="info-label">日時</div>
  <div>
    <div class="year">2021 年</div>
    <div class="day">7/18<small> [SUN]</small></div>
    <div class="time">11:00-16:00</div>
  </div>
</div>
<div class="info place">
  <div class="info-label">場所</div>
  <div>
    <div class="venue">Sunny Pawz 東大阪会場</div>
    <div class="addr">〒123-456<br>東大阪市若草台一丁目5番8号</div>
  </div>
</div>

<div class="photos">
  <div class="photo p1" role="img" aria-label="保護犬の写真（子犬）"></div>
  <div class="photo p2" role="img" aria-label="保護犬の写真（柴犬の子犬）"></div>
  <div class="photo p3" role="img" aria-label="保護犬の写真（トイプードル）"></div>
  <div class="photo p4" role="img" aria-label="保護犬の写真（ミックス犬）"></div>
</div>
<p class="waiting">まってるワン!</p>

<svg class="paw" style="left:120px;top:500px" width="34" height="34" viewBox="0 0 24 24"><circle cx="6" cy="9" r="2.3"/><circle cx="10" cy="5" r="2.3"/><circle cx="14" cy="5" r="2.3"/><circle cx="18" cy="9" r="2.3"/><ellipse cx="12" cy="15" rx="5" ry="4.2"/></svg>
<svg class="paw" style="left:680px;top:560px" width="34" height="34" viewBox="0 0 24 24"><circle cx="6" cy="9" r="2.3"/><circle cx="10" cy="5" r="2.3"/><circle cx="14" cy="5" r="2.3"/><circle cx="18" cy="9" r="2.3"/><ellipse cx="12" cy="15" rx="5" ry="4.2"/></svg>

<section class="section events">
  <div class="pill">イベント内容</div>
  <ul class="event-list">
    <li><svg viewBox="0 0 24 24"><circle cx="6" cy="9" r="2.3"/><circle cx="10" cy="5" r="2.3"/><circle cx="14" cy="5" r="2.3"/><circle cx="18" cy="9" r="2.3"/><ellipse cx="12" cy="15" rx="5" ry="4.2"/></svg>保護犬の新しいお家探し</li>
    <li><svg viewBox="0 0 24 24"><circle cx="6" cy="9" r="2.3"/><circle cx="10" cy="5" r="2.3"/><circle cx="14" cy="5" r="2.3"/><circle cx="18" cy="9" r="2.3"/><ellipse cx="12" cy="15" rx="5" ry="4.2"/></svg>トリマーによるワンコインお手入れ</li>
    <li><svg viewBox="0 0 24 24"><circle cx="6" cy="9" r="2.3"/><circle cx="10" cy="5" r="2.3"/><circle cx="14" cy="5" r="2.3"/><circle cx="18" cy="9" r="2.3"/><ellipse cx="12" cy="15" rx="5" ry="4.2"/></svg>わんちゃん用品フリマ販売</li>
    <li><svg viewBox="0 0 24 24"><circle cx="6" cy="9" r="2.3"/><circle cx="10" cy="5" r="2.3"/><circle cx="14" cy="5" r="2.3"/><circle cx="18" cy="9" r="2.3"/><ellipse cx="12" cy="15" rx="5" ry="4.2"/></svg>わんちゃんオリジナルプリントグッズ受注会<sup>（※1）</sup></li>
  </ul>
</section>

<section class="section notes">
  <div class="pill">ご来場の方へ</div>
  <ul class="note-list">
    <li>当日の参加犬はPicsnapにてご確認お願い致します。</li>
    <li>イベント内容は変更になる場合があります。</li>
    <li>愛犬同伴の場合、マナー用品の着用をお願い致します。</li>
    <li>会場が狭いため、入場制限を行う場合がございます。</li>
    <li>検温・アルコール消毒・マスク着用のご協力をお願い致します。</li>
  </ul>
</section>

<footer class="footer">
  <div class="org-mark"><span class="dot"></span>Sunny Pawz</div>
  <div class="org-text">
    主催　特定非営利活動法人Sunny Pawz<br>
    〒579-2208 枚方市桜木台四丁目3番21号<br>
    HP　https://sunnypawz2019.example-site.jp/<br>
    Picsnap　sunnypawz.2019
  </div>
</footer>
<p class="footnote">※当日の売上金は保護犬の活動費となります。（※1については一部）</p>
</body>
</html>
```